Innovative and exciting banner advert for real estate
Lots of freedom of design
#10 I like the way the 'save thousands in commission' is done with mixed size font. The 'save thousands' stands out very clearly which is important to us
Thanks.
Hi and thank you designers for your attention to our project, there are some great ideas coming in now.
A slight change to the brief:
In the blue screen, please remove 'money back guarantee' and replace with 'no hidden charges' from the green screen so each screen has only 3 bullet points.
Thanks
RPellow
Hi Designers
Please note, we do not require the logo in the adverts just the use of the logo colours as the base.
It is more important that the first line of text stands out. If you are going to insert the logo, please make it a minor element or as #4 has cleverly used it for the bullet points.
Thanks designers for your time and great ideas. #4 I like the way you have used the logo symbol in the bullet points, and that you have aligned the bullets points to the left, it looks good.
#5 the way that 'save thousands' and 'get the best price' stand out clearly is great, this is the message that we are trying to pass on to viewers, it is most important.
If there is any information you need please contact me directly, I will check messages.
Just to clarify, we do not require the logo in the adverts just the use of the logo colours as the base. These adverts are going to be used on our own site.
Regards
Thanks Hostmod for making that clear for designers.
Designers, we don't have images of the product we sell as we provide real estate services (not goods). If looking for inspiration for imagery, residential property is more appropriate than commercial property.
Thanks everyone.
Attention Designers!
PH is looking for static banner design which includes two individual advert frames.
Banner size : 450 wide x 225 high
I'm clarifying with our site technicians exactly what the frames should be.
We originally wanted two individual advert frames, 450 wide x 225 high, with no animation in the frames themselves. However, when trying to work within the Tandelvox fields, we couldn't elect the specific size we required and instead had to opt for a package deal.
I will upload a link to the real estate website template we will be using, the template has 'featured property' images in the centre of the homepage which we will be replacing with our two adverts. That is, we will not have the featured property on the home page at all.
http://skins.brovellanstudio.example/?theme=realestate2
Dear PH,
Is this animated gifs or flash?

```html
<!DOCTYPE html>
<html lang="en">
<head>
<meta charset="utf-8">
<title>Get the Best Price for Your Property</title>
<link rel="stylesheet" href="https://fonts.googleapis.com/css2?family=Arimo:wght@400;700&display=swap">
<style>
  :root {
    --bg-deep: #3c6810;
    --bg-mid: #5c901c;
    --bg-light: #7cb02e;
    --panel-top: #b4dc5c;
    --panel-bottom: #94c638;
    --panel-edge: #c8e87a;
    --headline: #2c5208;
    --bullet-text: #f2f8e4;
    --bullet-mark: #a8d850;
  }
  html, body {
    margin: 0;
    padding: 0;
    overflow: hidden;
    background: var(--bg-deep);
  }
  .banner {
    position: relative;
    width: 1200px;
    height: 600px;
    overflow: hidden;
    font-family: "Arimo", Arial, sans-serif;
    background:
      radial-gradient(ellipse 70% 60% at 55% 35%, var(--bg-light) 0%, var(--bg-mid) 50%, var(--bg-deep) 100%);
  }
  .headline-panel {
    position: absolute;
    left: 24px;
    top: 20px;
    width: 1160px;
    height: 320px;
    background: linear-gradient(180deg, var(--panel-top) 0%, var(--panel-bottom) 100%);
    border: 2px solid var(--panel-edge);
    box-shadow: 0 6px 18px rgba(20, 50, 0, 0.45);
    box-sizing: border-box;
  }
  .headline {
    position: absolute;
    left: 0;
    right: 0;
    top: 52px;
    margin: 0;
    padding-left: 220px;
    text-align: center;
    color: var(--headline);
    font-weight: 700;
    text-transform: uppercase;
    line-height: 1;
  }
  .headline .get {
    display: block;
    font-size: 96px;
    letter-spacing: 2px;
  }
  .headline .best-price {
    display: block;
    font-size: 64px;
    margin-top: 10px;
  }
  .headline .for-property {
    display: block;
    font-size: 36px;
    margin-top: 18px;
  }
  .benefits {
    position: absolute;
    left: 184px;
    top: 380px;
    margin: 0;
    padding: 0;
    list-style: none;
  }
  .benefits li {
    display: flex;
    align-items: center;
    height: 64px;
    color: var(--bullet-text);
    font-size: 29px;
    text-transform: uppercase;
    letter-spacing: 0.5px;
  }
  .benefits .mark {
    width: 30px;
    height: 30px;
    margin-right: 40px;
    flex: none;
  }
</style>
</head>
<body>
  <div class="banner">
    <div class="headline-panel"></div>
    <h1 class="headline">
      <span class="get">Get</span>
      <span class="best-price">The Best Price</span>
      <span class="for-property">For Your Property</span>
    </h1>
    <ul class="benefits">
      <li><svg class="mark" viewBox="0 0 30 30" aria-hidden="true"><rect x="3" y="3" width="24" height="24" fill="var(--bullet-mark)"/></svg>Feature rich marketing solutions</li>
      <li><svg class="mark" viewBox="0 0 30 30" aria-hidden="true"><rect x="3" y="3" width="24" height="24" fill="var(--bullet-mark)"/></svg>Professional tips, tools and strategies</li>
      <li><svg class="mark" viewBox="0 0 30 30" aria-hidden="true"><rect x="3" y="3" width="24" height="24" fill="var(--bullet-mark)"/></svg>0 % Commission</li>
    </ul>
  </div>
</body>
</html>
```